Pest Control Company needs business card!

Hi there, we need a business card designed for our new Pest Control Company. Ideally this card will be simple, yet feel elegant and high end. We want to use the colours Orange, Black and White. Please see our attached logo for the exact colours.

Business card details:

Phone - 0461 275 804
Name - Gavin Holloway
Email - Info@steadfastverminguard.com.au

We would also like to include the following list with dot points:

SERVICES / INSPECTIONS

Termites, Wood Borers, Ants, Cockroaches, Spiders, Fleas, Mice, Rats, Bed Bugs, & More!

```html
<!DOCTYPE html>
<html lang="en">
<head>
<meta charset="utf-8">
<title>Steadfast Vermin Guard – Business Card</title>
<link href="https://fonts.googleapis.com/css2?family=Montserrat:wght@400;500;600;700&display=swap" rel="stylesheet">
<style>
  :root {
    --orange: #ff7a0f;
    --orange-light: #fba11a;
    --orange-mid: #f97e0c;
    --orange-deep: #f55a10;
    --band-dark: #242424;
    --strip-black: #111111;
    --white: #ffffff;
    --muted: #d9d9d9;
  }
  html, body {
    margin: 0;
    padding: 0;
    width: 1200px;
    height: 686px;
    overflow: hidden;
    background: #ffffff;
  }
  .card {
    position: relative;
    width: 1200px;
    height: 686px;
    overflow: hidden;
    font-family: "Montserrat", Arial, sans-serif;
    color: var(--white);
  }
  .photo {
    position: absolute;
    top: 0;
    height: 303px;
  }
  .photo--cockroach {
    left: 0;
    width: 477px;
    background: radial-gradient(ellipse at 45% 45%, #5a5a5a 0%, #3c3c3c 55%, #6a6a6a 100%);
  }
  .photo--ant {
    left: 479px;
    width: 721px;
    background: linear-gradient(160deg, #3a3d3d 0%, #2b2e2e 45%, #5c5f5f 80%, #7a7c7c 100%);
  }
  .identity-band {
    position: absolute;
    top: 303px;
    left: 0;
    width: 1200px;
    height: 217px;
    background: var(--band-dark);
  }
  .person {
    position: absolute;
    left: 57px;
    top: 67px;
  }
  .person__name {
    margin: 0;
    font-size: 43px;
    font-weight: 700;
    line-height: 1;
    letter-spacing: 0.5px;
    text-transform: uppercase;
  }
  .person__name .surname { color: var(--orange); }
  .person__role {
    margin: 12px 0 0 3px;
    font-size: 24px;
    font-weight: 600;
    line-height: 1;
    text-transform: uppercase;
  }
  .brand {
    position: absolute;
    right: 50px;
    top: 40px;
    display: flex;
    align-items: center;
    gap: 12px;
  }
  .brand__name {
    margin: 0;
    font-size: 26px;
    font-weight: 700;
    line-height: 1;
    color: var(--orange);
    text-transform: uppercase;
    white-space: nowrap;
  }
  .brand__dot {
    width: 30px;
    height: 30px;
    border-radius: 50%;
    background: var(--orange);
  }
  .services {
    position: absolute;
    right: 50px;
    top: 98px;
    width: 560px;
  }
  .services__title {
    margin: 0 0 10px;
    font-size: 14px;
    font-weight: 700;
    letter-spacing: 1px;
    color: var(--orange);
    text-transform: uppercase;
  }
  .services__list {
    margin: 0;
    padding: 0;
    list-style: none;
    display: grid;
    grid-template-columns: repeat(5, auto);
    column-gap: 16px;
    row-gap: 8px;
    font-size: 14px;
    font-weight: 500;
    color: var(--muted);
  }
  .services__list li {
    display: flex;
    align-items: center;
    gap: 7px;
    white-space: nowrap;
  }
  .services__list li::before {
    content: "";
    width: 6px;
    height: 6px;
    border-radius: 50%;
    background: var(--orange);
    flex: none;
  }
  .divider-strip {
    position: absolute;
    top: 520px;
    left: 0;
    width: 1200px;
    height: 23px;
    background: var(--strip-black);
  }
  .contacts {
    position: absolute;
    top: 543px;
    left: 0;
    width: 1200px;
    height: 143px;
    display: flex;
  }
  .contact {
    position: relative;
    height: 100%;
    display: flex;
    flex-direction: column;
    align-items: center;
    justify-content: center;
    padding-top: 30px;
    box-sizing: border-box;
    text-align: center;
    font-size: 22px;
    font-weight: 400;
    line-height: 1.3;
  }
  .contact p { margin: 0; }
  .contact--address { width: 398px; background: var(--orange-light); }
  .contact--phone { width: 400px; background: var(--orange-mid); }
  .contact--web { width: 402px; background: var(--orange-deep); font-size: 20px; }
  .contact__icon {
    position: absolute;
    top: -35px;
    left: 50%;
    margin-left: -35px;
    width: 70px;
    height: 70px;
    border-radius: 50%;
    background: linear-gradient(180deg, #ff9a1a 0%, #f26a0a 100%);
    box-shadow: 0 4px 0 rgba(0,0,0,0.25);
    display: flex;
    align-items: center;
    justify-content: center;
  }
  .contact__icon svg { width: 32px; height: 32px; fill: var(--white); }
</style>
</head>
<body>
  <div class="card">
    <div class="photo photo--cockroach" role="img" aria-label="Close-up monochrome photograph of a cockroach"></div>
    <div class="photo photo--ant" role="img" aria-label="Close-up monochrome photograph of an ant on a wooden surface"></div>

    <section class="identity-band">
      <div class="person">
        <h1 class="person__name">Gavin <span class="surname">Holloway</span></h1>
        <p class="person__role">General Manager</p>
      </div>
      <div class="brand">
        <p class="brand__name">Steadfast Vermin Guard</p>
        <span class="brand__dot"></span>
      </div>
      <div class="services">
        <p class="services__title">Services / Inspections</p>
        <ul class="services__list">
          <li>Termites</li>
          <li>Wood Borers</li>
          <li>Ants</li>
          <li>Cockroaches</li>
          <li>Spiders</li>
          <li>Fleas</li>
          <li>Mice</li>
          <li>Rats</li>
          <li>Bed Bugs</li>
          <li>&amp; More!</li>
        </ul>
      </div>
    </section>

    <div class="divider-strip"></div>

    <section class="contacts">
      <div class="contact contact--address">
        <span class="contact__icon">
          <svg viewBox="0 0 24 24" aria-hidden="true"><path d="M12 2a7 7 0 0 0-7 7c0 5.2 7 13 7 13s7-7.8 7-13a7 7 0 0 0-7-7zm0 9.5A2.5 2.5 0 1 1 12 6.5a2.5 2.5 0 0 1 0 5z"/></svg>
        </span>
        <p>123, street, your city,</p>
        <p>Australia 456123</p>
      </div>
      <div class="contact contact--phone">
        <span class="contact__icon">
          <svg viewBox="0 0 24 24" aria-hidden="true"><path d="M20 15.5c-1.2 0-2.4-.2-3.6-.6a1 1 0 0 0-1 .25l-2.2 2.2a15.1 15.1 0 0 1-6.6-6.6l2.2-2.2a1 1 0 0 0 .25-1A11.4 11.4 0 0 1 8.5 4a1 1 0 0 0-1-1H4a1 1 0 0 0-1 1 17 17 0 0 0 17 17 1 1 0 0 0 1-1v-3.5a1 1 0 0 0-1-1z"/></svg>
        </span>
        <p>0461 275 804</p>
      </div>
      <div class="contact contact--web">
        <span class="contact__icon">
          <svg viewBox="0 0 24 24" aria-hidden="true"><path d="M12 2a10 10 0 1 0 0 20 10 10 0 0 0 0-20zm6.9 6h-2.9a15.6 15.6 0 0 0-1.4-3.6A8 8 0 0 1 18.9 8zM12 4c.8 1.2 1.5 2.5 1.9 4h-3.8c.4-1.5 1.1-2.8 1.9-4zM4.3 14a8.2 8.2 0 0 1 0-4h3.4a16.5 16.5 0 0 0 0 4H4.3zm.8 2h2.9c.3 1.3.8 2.5 1.4 3.6A8 8 0 0 1 5.1 16zM8 8H5.1a8 8 0 0 1 4.3-3.6C8.8 5.5 8.3 6.7 8 8zm4 12c-.8-1.2-1.5-2.5-1.9-4h3.8c-.4 1.5-1.1 2.8-1.9 4zm2.3-6H9.7a14.7 14.7 0 0 1 0-4h4.6a14.7 14.7 0 0 1 0 4zm.3 5.6c.6-1.1 1.1-2.3 1.4-3.6h2.9a8 8 0 0 1-4.3 3.6zm1.7-5.6a16.5 16.5 0 0 0 0-4h3.4a8.2 8.2 0 0 1 0 4h-3.4z"/></svg>
        </span>
        <p>Info@steadfastverminguard.com.au</p>
        <p>www.steadfastverminguard.com</p>
      </div>
    </section>
  </div>
</body>
</html>
```